Legal Stationary

A full set of stationery is required
The image and logo, along with colour, are set and attached.
The style should be modern, clean, and corporate. Not just a basic template off the web.
In addition to the address/website/email/phone fields for DX and KWT number, with the text “the firm is authorised and regulated by the KWT”
All files in all formats will be needed to allow editing after. Initial setup of templates will be required, and details for 4 business cards will be supplied.
Target Market(s)
Consumers of legal services
Industry/Entity Type
Legal

```html
<!DOCTYPE html>
<html lang="en">
<head>
<meta charset="utf-8">
<title>Marlow Law Stationery</title>
<link href="https://fonts.googleapis.com/css2?family=Montserrat:wght@400;500;600;700&family=Lato:wght@300;400;700&display=swap" rel="stylesheet">
<style>
:root{
  --brand-blue:#253a94;
  --ink:#222;
  --dark:#2a2a2a;
  --muted:#555;
  --body-text:#666;
  --paper:#ffffff;
  --backdrop:#d2d2d2;
  --rule:#cfcfcf;
  --stamp:#c1272d;
}
*{margin:0;padding:0;box-sizing:border-box}
html,body{width:1200px;height:768px;overflow:hidden}
body{background:var(--backdrop);position:relative;font-family:'Lato',sans-serif;color:var(--ink)}
.piece{position:absolute;background:var(--paper);box-shadow:0 2px 6px rgba(0,0,0,.12)}
.wordmark{font-family:'Montserrat',sans-serif;font-weight:500;color:var(--brand-blue);white-space:nowrap;line-height:1;letter-spacing:.01em}
.wordmark.on-blue{color:#fff}

/* Letterhead */
.letterhead{left:66px;top:74px;width:426px;height:609px}
.letterhead .wordmark{position:absolute;left:36px;top:39px;font-size:16px}
.letterhead .address{position:absolute;left:231px;top:31px;font-family:'Montserrat',sans-serif;font-size:7px;line-height:10.2px}
.letterhead .divider{position:absolute;left:311px;top:29px;width:1px;height:36px;background:#999}
.letterhead .contacts{position:absolute;left:319px;top:31px;font-family:'Montserrat',sans-serif;font-size:7px;line-height:10.2px}
.contacts .icon{display:inline-block;width:5px;height:5px;margin-right:3px;background:var(--brand-blue);border-radius:50%;vertical-align:middle}
.contacts .icon.sq{border-radius:1px}
.letterhead .recipient{position:absolute;left:36px;top:158px;font-size:9px;font-weight:700}
.letterhead .recipient small{display:block;font-size:6.2px;margin-top:3px}
.letterhead .date{position:absolute;right:35px;top:170px;font-size:6.3px;color:var(--muted)}
.letterhead .body{position:absolute;left:36px;top:202px;width:355px;font-size:6.3px;font-weight:400;line-height:10.4px;color:var(--body-text);text-align:justify}
.letterhead .body p{margin-bottom:10.4px}
.letterhead .signature{position:absolute;left:36px;top:438px;width:92px;height:24px;background:#ececec}
.regulation{font-family:'Montserrat',sans-serif;color:var(--ink);white-space:nowrap}
.letterhead .regulation{position:absolute;left:0;right:0;top:577px;text-align:center;font-size:7.4px}
.footer-bar{position:absolute;left:0;right:0;bottom:0;display:flex;gap:3px}
.footer-bar .blue{background:var(--brand-blue);flex:1}
.footer-bar .black{background:#1b1b1b}
.letterhead .footer-bar{height:13px}
.letterhead .footer-bar .black{width:59px}

/* Business card front */
.card{border-radius:8px;overflow:hidden}
.card-front{left:525px;top:74px;width:250px;height:146px}
.card-front .wordmark{position:absolute;left:0;right:0;top:26px;text-align:center;font-size:20px}
.card-front .band{position:absolute;left:0;right:0;top:77px;height:36px;display:flex}
.card-front .name-block{width:126px;background:var(--brand-blue);color:#fff;text-align:right;padding:7px 8px 0 0;font-family:'Montserrat',sans-serif}
.name-block strong{display:block;font-size:10.5px;font-weight:700;letter-spacing:.02em}
.name-block span{font-size:6.8px}
.card-front .contact-block{flex:1;background:var(--dark);color:#fff;font-family:'Montserrat',sans-serif;font-size:7px;line-height:10.3px;padding:3px 0 0 9px}
.contact-block .icon{display:inline-block;width:5px;height:5px;margin-right:4px;background:#fff;border-radius:50%;vertical-align:middle}
.card-front .card-address{position:absolute;left:0;right:0;top:128px;text-align:center;font-family:'Montserrat',sans-serif;font-size:6.8px}

/* Business card back */
.card-back{left:525px;top:235px;width:251px;height:147px;background:var(--brand-blue)}
.card-back .wordmark{position:absolute;left:0;right:0;top:61px;text-align:center;font-size:24px}

/* Envelope with flap */
.envelope-flap{left:800px;top:73px;width:331px;height:145px}
.envelope-flap svg{position:absolute;left:0;top:0}
.envelope-flap .wordmark{position:absolute;left:0;right:0;top:23px;text-align:center;font-size:9px}
.envelope-flap .web{position:absolute;left:0;right:0;top:120px;text-align:center;font-family:'Montserrat',sans-serif;font-size:5.5px;letter-spacing:.15em}

/* Envelope front */
.envelope-front{left:800px;top:236px;width:331px;height:147px}
.envelope-front .wordmark{position:absolute;left:14px;top:21px;font-size:11px}
.envelope-front .divider{position:absolute;left:104px;top:15px;width:1px;height:24px;background:#999}
.envelope-front .address{position:absolute;left:109px;top:16px;font-family:'Montserrat',sans-serif;font-size:4.6px;line-height:7px}
.envelope-front .stamp{position:absolute;left:282px;top:11px;width:33px;height:40px;background:var(--stamp);outline:2px dotted #fff;box-shadow:0 0 0 2px #ddd}
.envelope-front .regulation{position:absolute;left:14px;top:129px;font-size:4.8px}
.envelope-front .footer-bar{height:6px}
.envelope-front .footer-bar .black{width:56px}

/* Closed notebook */
.notebook-closed{left:552px;top:418px;width:188px;height:263px;background:var(--brand-blue);box-shadow:2px 3px 6px rgba(0,0,0,.2)}
.notebook-closed .wordmark{position:absolute;left:0;right:0;top:125px;text-align:center;font-size:15px}
.coil{position:absolute;width:16px;background:repeating-linear-gradient(to bottom,transparent 0 3px,#6d6d6d 3px 4px,#cfcfcf 4px 6px,#6d6d6d 6px 7px,transparent 7px 11.5px)}
.notebook-closed-coil{left:546px;top:424px;height:252px}

/* Open notebook */
.notebook-open{left:760px;top:415px;width:370px;height:261px;background:transparent;box-shadow:none}
.page{position:absolute;top:0;width:184px;height:261px;background:#f8f8f8;box-shadow:0 2px 5px rgba(0,0,0,.15)}
.page.left{left:0}
.page.right{left:186px}
.page .wordmark{position:absolute;left:17px;top:20px;font-size:7px}
.page .date-field{position:absolute;right:16px;top:37px;font-size:3.5px;color:#888}
.page .lines{position:absolute;left:17px;right:14px;top:46px;height:196px;background:repeating-linear-gradient(to bottom,transparent 0 10px,var(--rule) 10px 10.5px)}
.page .regulation{position:absolute;left:0;right:0;top:250px;text-align:center;font-size:3.2px}
.page .footer-bar{height:4px}
.page .footer-bar .black{width:24px}
.notebook-open-coil{left:935px;top:420px;height:250px}
</style>
</head>
<body>

<!-- Letterhead -->
<section class="piece letterhead" aria-label="Letterhead">
  <div class="wordmark">MARLOW LAW</div>
  <div class="address">The Quarry<br>42 Canal Row<br>Ashford, AF2 7TD</div>
  <div class="divider"></div>
  <div class="contacts">
    <div><span class="icon sq"></span>(555) 210-4837</div>
    <div><span class="icon sq"></span>info@marlowlaw.com</div>
    <div><span class="icon"></span>www.marlowlaw.com</div>
  </div>
  <div class="recipient">Dear. Mrs Clara Jane Holt<small>Chief Director</small></div>
  <div class="date">Date: 17-June-2025</div>
  <div class="body">
    <p>Lorem ipsum dolor sit amet, consectetur adipiscing elit, sed do eiusmod tempor incididunt ut labore et dolore magna aliqua. Sollicitudin ac orci phasellus egestas tellus rutrum tellus. Euismod elementum nisi quis eleifend quam adipiscing vitae proin sagittis. Egestas sed tempus urna et pharetra pharetra. Quis blandit turpis cursus in hac habitasse. Sed velit dignissim sodales ut eu. Ac auctor augue mauris augue neque. In arcu cursus euismod quis viverra nibh cras pulvinar mattis. Libero justo laoreet sit amet. Felis eget nunc lobortis mattis aliquam faucibus purus in. Pulvinar etiam non quam lacus suspendisse faucibus. Odio tempor orci dapibus ultrices. Velit dignissim sodales ut eu sem integer vitae justo. Fermentum et sollicitudin ac orci phasellus egestas. Pharetra vel turpis nunc eget lorem dolor sed. Sed turpis tincidunt id aliquet risus feugiat in ante. Mus mauris vitae ultricies leo integer malesuada nunc vel. Rhoncus urna neque viverra justo nec ultrices dui. Ut placerat orci nulla pellentesque dignissim enim sit amet.</p>
    <p>Bibendum arcu vitae elementum curabitur vitae nunc. Nunc pulvinar sapien et ligula ullamcorper malesuada. At elementum eu facilisis sed. Erat pellentesque adipiscing commodo elit at imperdiet dui accumsan sit. Nunc scelerisque viverra mauris in aliquam sem fringilla. In vitae turpis massa sed. Volutpat ac tincidunt vitae semper quis lectus nulla at. Massa placerat duis ultricies lacus sed turpis. Dui vivamus arcu felis bibendum ut tristique et egestas. Blandit aliquam etiam erat velit scelerisque in dictum non consectetur. Id neque aliquam vestibulum morbi blandit cursus risus at. Sed egestas egestas fringilla phasellus faucibus scelerisque eleifend donec. Ornare quam viverra orci sagittis eu volutpat odio facilisis. Volutpat sed cras ornare arcu dui vivamus arcu. Interdum consectetur libero id faucibus nisl.</p>
    <p>Viverra mauris in aliquam sem. Mattis molestie a iaculis at erat pellentesque adipiscing commodo elit. Sit amet volutpat consequat mauris nunc. Aliquam nulla facilisi cras fermentum. Sed turpis tincidunt id aliquet risus feugiat. Augue neque gravida in fermentum et sollicitudin ac orci.</p>
  </div>
  <div class="signature" role="img" aria-label="Handwritten signature of the sender"></div>
  <div class="regulation">The firm is authorised and regulated by the KWT&nbsp; / &nbsp;DX No - 418207 /&nbsp; KWT No - 418207</div>
  <div class="footer-bar"><div class="blue"></div><div class="black"></div></div>
</section>

<!-- Business card, front -->
<section class="piece card card-front" aria-label="Business card front">
  <div class="wordmark">MARLOW LAW</div>
  <div class="band">
    <div class="name-block"><strong>HANA PEREIRA</strong><span>Founder &amp; CEO</span></div>
    <div class="contact-block">
      <div><span class="icon"></span>(555) 210-4837</div>
      <div><span class="icon"></span>info@marlowlaw.com</div>
      <div><span class="icon"></span>www.marlowlaw.com</div>
    </div>
  </div>
  <div class="card-address">The Quarry, 42 Canal Row, Ashford, AF2 7TD</div>
</section>

<!-- Business card, back -->
<section class="piece card card-back" aria-label="Business card back">
  <div class="wordmark on-blue">MARLOW LAW</div>
</section>

<!-- Envelope, flap side -->
<section class="piece envelope-flap" aria-label="Envelope back">
  <svg width="331" height="145" viewBox="0 0 331 145" aria-hidden="true">
    <path d="M0 0 H331 L322 35 Q318 52 300 52 H30 Q13 52 8 35 Z" fill="var(--brand-blue)"/>
  </svg>
  <div class="wordmark on-blue">MARLOW LAW</div>
  <div class="web">www.quietharbourpath.com</div>
</section>

<!-- Envelope, address side -->
<section class="piece envelope-front" aria-label="Envelope front">
  <div class="wordmark">MARLOW LAW</div>
  <div class="divider"></div>
  <div class="address">The Quarry<br>42 Canal Row<br>Ashford, AF2 7TD</div>
  <div class="stamp" role="img" aria-label="Postage stamp"></div>
  <div class="regulation">The firm is authorised and regulated by the KWT&nbsp; / &nbsp;DX No - 418207 /&nbsp; KWT No - 418207</div>
  <div class="footer-bar"><div class="blue"></div><div class="black"></div></div>
</section>

<!-- Closed notebook -->
<section class="piece notebook-closed" aria-label="Notebook cover">
  <div class="wordmark on-blue">MARLOW LAW</div>
</section>
<div class="coil notebook-closed-coil" aria-hidden="true"></div>

<!-- Open notebook -->
<section class="piece notebook-open" aria-label="Notebook pages">
  <div class="page left">
    <div class="wordmark">MARLOW LAW</div>
    <div class="date-field">Date:......./......./.........</div>
    <div class="lines"></div>
    <div class="regulation">The firm is authorised and regulated by the KWT / DX No - 418207 / KWT No - 418207</div>
    <div class="footer-bar"><div class="blue"></div><div class="black"></div></div>
  </div>
  <div class="page right">
    <div class="wordmark">MARLOW LAW</div>
    <div class="date-field">Date:......./......./.........</div>
    <div class="lines"></div>
    <div class="regulation">The firm is authorised and regulated by the KWT / DX No - 418207 / KWT No - 418207</div>
    <div class="footer-bar"><div class="blue"></div><div class="black"></div></div>
  </div>
</section>
<div class="coil notebook-open-coil" aria-hidden="true"></div>

</body>
</html>
```